" Somos a única empresa no Brasil autorizada a importar e comercializar Verdex Fertilizantes. Vamos iniciar a divulgação para comercialização do produto, que embarca nano tecnologia de ponta, para o público consumidor. "

```html
<!DOCTYPE html>
<html lang="pt-BR">
<head>
<meta charset="UTF-8">
<title>Lumina Fertilizantes — Nano Ureia</title>
<link href="https://fonts.googleapis.com/css2?family=Montserrat:wght@400;600;800;900&display=swap" rel="stylesheet">
<style>
:root{
  --purple:#6c1a57;
  --purple-dark:#541343;
  --lime:#b6c928;
  --paper:#f4f3f4;
  --card:#ffffff;
  --ink:#3a2a36;
  --muted:#6d5f69;
}
*{box-sizing:border-box;margin:0;padding:0}
html,body{width:1200px;height:1200px;overflow:hidden;background:#e6e4e6}
body{font-family:'Montserrat',sans-serif;color:var(--ink)}
.flyer{position:relative;width:1200px;height:1200px;background:var(--paper);overflow:hidden}
.top-band{position:absolute;left:0;top:0;width:1200px;height:90px}
.brand{position:absolute;right:60px;top:44px;display:flex;align-items:center;gap:12px;
  font-weight:800;font-size:30px;color:var(--purple);letter-spacing:.5px}
.brand-dot{width:18px;height:18px;border-radius:50%;background:var(--lime)}
.section-title{position:absolute;left:60px;font-weight:900;color:var(--purple);text-transform:uppercase}
.about-title{top:110px;font-size:58px;letter-spacing:1px}
.about-band{position:absolute;left:0;top:192px;width:1200px;height:150px;background:var(--purple);
  padding:22px 60px;color:#fff;font-size:20px;line-height:1.45}
.about-band p+p{margin-top:8px}
.why-accent{position:absolute;left:0;top:350px;width:1200px;height:70px}
.why-title{top:362px;font-size:40px;letter-spacing:1px}
.cards{position:absolute;left:60px;top:428px;width:1080px;display:grid;grid-template-columns:repeat(4,1fr);gap:18px}
.card{background:var(--card);border-radius:8px;padding:14px 16px 14px;box-shadow:0 2px 6px rgba(80,20,60,.12);min-height:150px}
.card-icon{width:24px;height:24px;margin-bottom:6px}
.card h3{font-size:15px;font-weight:800;color:var(--purple);margin-bottom:5px}
.card p{font-size:12px;line-height:1.4;color:var(--muted)}
.benefits{position:absolute;left:60px;top:606px;width:1080px;display:flex;justify-content:space-between;list-style:none}
.benefit{display:flex;align-items:flex-start;gap:8px;font-size:15px;font-weight:800;color:var(--purple);text-transform:uppercase;line-height:1.15;width:200px}
.benefit svg{flex:0 0 26px;margin-top:2px}
.gallery{position:absolute;left:0;top:670px;width:1200px;height:530px;display:grid;gap:6px;
  grid-template-columns:repeat(12,1fr);grid-template-rows:260px 264px}
.p1{grid-column:1/5;background:linear-gradient(135deg,#a8242a,#d9483a 45%,#6f8f3a)}
.p2{grid-column:5/9;background:linear-gradient(135deg,#2f6a2e,#4c8a3a 50%,#bda34a)}
.p3{grid-column:9/13;background:linear-gradient(135deg,#9b7fb5,#c9b7d6 50%,#4f7d3a)}
.p4{grid-column:1/4;background:linear-gradient(160deg,#7f8c6a,#4c5e3a)}
.p5{grid-column:4/7;background:linear-gradient(180deg,#c8c6b8,#7e8c5a)}
.p6{grid-column:7/10;background:linear-gradient(180deg,#b7c2c6,#4e7a34)}
.p7{grid-column:10/13;background:linear-gradient(180deg,#d9cdb0,#6a7e40)}
.lime-edge{position:absolute;left:0;bottom:0;width:26px;height:300px;background:var(--lime)}
</style>
</head>
<body>
<main class="flyer">
  <svg class="top-band" viewBox="0 0 1200 90" aria-hidden="true">
    <polygon points="0,0 760,0 700,30 0,30" fill="#6c1a57"/>
    <polygon points="700,30 760,0 800,0 740,30" fill="#b6c928"/>
  </svg>

  <div class="brand"><span class="brand-dot"></span>Lumina Fertilizantes</div>

  <h1 class="section-title about-title">Quem Somos</h1>
  <section class="about-band">
    <p>Somos uma empresa brasileira e nossa missão é revolucionar a agricultura por meio de tecnologia inovadora e comprovada.</p>
    <p>Oferecemos aos produtores nanofertilizantes que aumentam a produtividade dos cultivos, reduzem os custos operacionais e minimizam os impactos ambientais, por meio da nanotecnologia.</p>
  </section>

  <svg class="why-accent" viewBox="0 0 1200 70" aria-hidden="true">
    <polygon points="620,70 1200,20 1200,34 660,70" fill="#b6c928"/>
  </svg>
  <h2 class="section-title why-title">Por que Nano Ureia?</h2>

  <div class="cards">
    <article class="card">
      <svg class="card-icon" viewBox="0 0 24 24"><circle cx="12" cy="12" r="4" fill="none" stroke="#6c1a57" stroke-width="2"/><path d="M12 2v4M12 18v4M2 12h4M18 12h4" stroke="#6c1a57" stroke-width="2"/></svg>
      <h3>Produtividade</h3>
      <p>Aumenta a produção e a qualidade das colheitas com maior aproveitamento do fertilizante aplicado.</p>
    </article>
    <article class="card">
      <svg class="card-icon" viewBox="0 0 24 24"><path d="M4 20C4 10 10 4 20 4c0 10-6 16-16 16z" fill="none" stroke="#6c1a57" stroke-width="2"/></svg>
      <h3>Sustentabilidade</h3>
      <p>Preserva o meio ambiente, evita lixiviação e volatilização, reduz impacto no solo, ar e água.</p>
    </article>
    <article class="card">
      <svg class="card-icon" viewBox="0 0 24 24"><text x="5" y="19" font-size="20" font-weight="800" fill="#6c1a57" font-family="Montserrat,sans-serif">$</text></svg>
      <h3>Economia</h3>
      <p>Mais produtividade com menor quantidade de fertilizante, reduzindo custos operacionais.</p>
    </article>
    <article class="card">
      <svg class="card-icon" viewBox="0 0 24 24"><path d="M12 3l2.5 6.5L21 12l-6.5 2.5L12 21l-2.5-6.5L3 12l6.5-2.5z" fill="none" stroke="#6c1a57" stroke-width="2"/></svg>
      <h3>Eficiência</h3>
      <p>+90% de absorção foliar. Até 20% mais eficiência. Fórmulas biodegradáveis e eco-friendly.</p>
    </article>
  </div>

  <ul class="benefits">
    <li class="benefit"><svg width="26" height="20" viewBox="0 0 26 20"><polygon points="0,20 13,0 26,20 13,13" fill="#b6c928"/></svg>Maior eficiência de absorção</li>
    <li class="benefit"><svg width="26" height="20" viewBox="0 0 26 20"><polygon points="0,0 13,20 26,0 13,7" fill="#b6c928"/></svg>Menor perda por volatilização</li>
    <li class="benefit"><svg width="26" height="20" viewBox="0 0 26 20"><polygon points="0,20 13,0 26,20 13,13" fill="#b6c928"/></svg>Melhor para o solo e o ambiente</li>
    <li class="benefit"><svg width="26" height="20" viewBox="0 0 26 20"><polygon points="0,20 13,0 26,20 13,13" fill="#b6c928"/></svg>Tecnologia nano comprovada</li>
    <li class="benefit"><svg width="26" height="20" viewBox="0 0 26 20"><polygon points="0,20 13,0 26,20 13,13" fill="#b6c928"/></svg>Melhor resposta das culturas</li>
  </ul>

  <section class="gallery">
    <div class="photo p1" role="img" aria-label="Foto de morangos, abobrinhas e legumes frescos"></div>
    <div class="photo p2" role="img" aria-label="Foto de hortaliças verdes e frutas variadas"></div>
    <div class="photo p3" role="img" aria-label="Foto de couve-flor roxa e folhas verdes"></div>
    <div class="photo p4" role="img" aria-label="Foto de agricultora cuidando da horta"></div>
    <div class="photo p5" role="img" aria-label="Foto de drone pulverizando uma lavoura"></div>
    <div class="photo p6" role="img" aria-label="Foto de avião agrícola sobre plantação em linhas"></div>
    <div class="photo p7" role="img" aria-label="Foto de trator pulverizando o campo"></div>
  </section>
  <div class="lime-edge" aria-hidden="true"></div>
</main>
</body>
</html>
```